Sales Funnel Infographic

Attached is our sale funnel graphic. We want to rebuild it from scratch as a vector Infographic, preferably .ai file. It will be used on our website & all sales collateral - both web and print.

This is a cornerstone of our marketing to illustrate to our potential clients what we do. We build sales engines for startup companies who don't yet have a department for sales and/or a systematic strategy for sales & marketing.

We will keep the basic funnel design, the copy, the order & relationships - by relationships I mean the arrows/connections between the pieces.

Examples of funnels I like:

http://www.plovrane.com/wp-content/uploads/2012/02/inbound-marketing-funnel.jpg

http://www.quelmarin.com/~/media/ideas%20blog%20images/video-for-sales-infographic.ashx

http://gravelmintyarchive.files.pagetrellis.com/2014/01/3d-funnel-design_01.jpg?w=700

Here's our website: http://ferncrow.com

our colors: corporate blue: #00144F
font: Titillium Web from Google Fonts

Final size should be 9x16 ratio including white space = tall version of HD widescreen

Target Market(s)

Funded businesses and silicon valley startups who are looking to hire us to create a sales engine for them.

Industry/Entity Type

Marketing

Font styles to use
Sans Serif

Requirements
Must have
• Vector .ai format
Basic Funnel Shape
All copy from attachment & relationships
white background
Nice to have
• optional color background
Should not have
• super-tall format

```html
<!DOCTYPE html>
<html lang="en">
<head>
<meta charset="utf-8">
<title>KEEN Growth Engine</title>
<link href="https://fonts.googleapis.com/css2?family=Titillium+Web:wght@400;600;700;900&family=Open+Sans:wght@400;600&display=swap" rel="stylesheet">
<style>
  :root{
    --corporate-blue:#00144F;
    --accent-red:#C0392B;
    --white:#FFFFFF;
    --ink:#00144F;
  }
  html,body{margin:0;padding:0;overflow:hidden;background:var(--white);}
  .canvas{position:relative;width:675px;height:1200px;overflow:hidden;background:var(--white);font-family:"Open Sans",Arial,sans-serif;}
  .top-band{position:absolute;left:0;top:0;width:675px;height:38px;background:var(--accent-red);}
  .header{position:absolute;left:0;top:38px;width:675px;height:167px;background:var(--corporate-blue);color:var(--white);text-align:center;}
  .header h1{margin:0;padding-top:20px;font-family:"Titillium Web",Arial,sans-serif;font-weight:900;font-size:50px;line-height:54px;letter-spacing:0.4px;}
  .header p{margin:4px auto 0;width:440px;font-family:"Open Sans",Arial,sans-serif;font-size:23px;line-height:32px;font-weight:400;}
  .funnel{position:absolute;left:0;top:0;width:675px;height:1200px;}
  .stage-label{font-family:"Titillium Web",Arial,sans-serif;font-weight:900;font-size:24.5px;fill:var(--white);text-anchor:middle;letter-spacing:0.2px;}
  .step-number{font-family:"Titillium Web",Arial,sans-serif;font-weight:700;font-size:18px;fill:var(--white);text-anchor:middle;}
  .step-text{font-family:"Open Sans",Arial,sans-serif;font-size:13.5px;fill:var(--ink);}
  .brand-name{position:absolute;left:44px;top:1102px;font-family:"Titillium Web",Arial,sans-serif;font-weight:700;font-size:46px;line-height:60px;letter-spacing:6px;color:var(--corporate-blue);}
  .web-box{position:absolute;left:392px;top:1102px;width:283px;height:60px;background:var(--corporate-blue);color:var(--white);font-family:"Open Sans",Arial,sans-serif;font-size:24px;line-height:60px;text-align:center;}
</style>
</head>
<body>
<div class="canvas">
  <div class="top-band"></div>
  <header class="header">
    <h1>KEEN Growth Engine</h1>
    <p>A proven process to drive predictable revenue and growth</p>
  </header>

  <svg class="funnel" viewBox="0 0 675 1200" aria-label="Seven-stage growth funnel">
    <defs>
      <linearGradient id="g-gold" x1="0" x2="1"><stop offset="0" stop-color="#B8924E"/><stop offset=".55" stop-color="#D8B475"/><stop offset="1" stop-color="#C29D5C"/></linearGradient>
      <linearGradient id="g-red" x1="0" x2="1"><stop offset="0" stop-color="#C92C2C"/><stop offset=".55" stop-color="#EA3B3B"/><stop offset="1" stop-color="#D23030"/></linearGradient>
      <linearGradient id="g-blue" x1="0" x2="1"><stop offset="0" stop-color="#0A2A6E"/><stop offset=".45" stop-color="#0096DA"/><stop offset="1" stop-color="#00AEEF"/></linearGradient>
      <linearGradient id="g-green" x1="0" x2="1"><stop offset="0" stop-color="#0B7C48"/><stop offset=".55" stop-color="#00A85A"/><stop offset="1" stop-color="#02954F"/></linearGradient>
      <linearGradient id="g-yellow" x1="0" x2="1"><stop offset="0" stop-color="#E8A91C"/><stop offset=".55" stop-color="#FFCB2F"/><stop offset="1" stop-color="#F4BA22"/></linearGradient>
      <linearGradient id="g-black" x1="0" x2="1"><stop offset="0" stop-color="#1E1E1E"/><stop offset=".55" stop-color="#444444"/><stop offset="1" stop-color="#2A2A2A"/></linearGradient>
      <linearGradient id="g-orange" x1="0" x2="1"><stop offset="0" stop-color="#D2622E"/><stop offset=".55" stop-color="#EE7D3C"/><stop offset="1" stop-color="#E06F34"/></linearGradient>
    </defs>

    <g class="stage">
      <path d="M38 263 L47 352 A168 16 0 0 0 383 352 L392 263 Z" fill="url(#g-gold)"/>
      <ellipse cx="215" cy="263" rx="177" ry="17" fill="#A8894A"/>
      <text class="stage-label" x="215" y="321">Vision &amp; Goals</text>
    </g>
    <g class="stage">
      <path d="M48 402 L56 486 A159 15 0 0 0 374 486 L382 402 Z" fill="url(#g-red)"/>
      <ellipse cx="215" cy="402" rx="167" ry="16" fill="#B52B2B"/>
      <text class="stage-label" x="215" y="444">Customer-Centric</text>
      <text class="stage-label" x="215" y="470">Strategy</text>
    </g>
    <g class="stage">
      <path d="M60 532 L69 609 A146 14 0 0 0 361 609 L370 532 Z" fill="url(#g-blue)"/>
      <ellipse cx="215" cy="532" rx="155" ry="14" fill="#001A5C"/>
      <text class="stage-label" x="215" y="572">Foundational</text>
      <text class="stage-label" x="215" y="598">Tools</text>
    </g>
    <g class="stage">
      <path d="M70 650 L78 722 A137 13 0 0 0 352 722 L360 650 Z" fill="url(#g-green)"/>
      <ellipse cx="215" cy="650" rx="145" ry="13" fill="#0E5A40"/>
      <text class="stage-label" x="215" y="690">Demand</text>
      <text class="stage-label" x="215" y="715">Generation</text>
    </g>
    <g class="stage">
      <path d="M80 762 L88 833 A127 12 0 0 0 342 833 L350 762 Z" fill="url(#g-yellow)"/>
      <ellipse cx="215" cy="762" rx="135" ry="12" fill="#C79A2E"/>
      <text class="stage-label" x="215" y="800">Qualify, Develop</text>
      <text class="stage-label" x="215" y="825">Close</text>
    </g>
    <g class="stage">
      <path d="M92 868 L100 928 A115 11 0 0 0 330 928 L338 868 Z" fill="url(#g-black)"/>
      <ellipse cx="215" cy="868" rx="123" ry="11" fill="#111111"/>
      <text class="stage-label" x="215" y="912">Growth &amp; Scale</text>
    </g>
    <g class="stage">
      <path d="M102 960 L110 1020 A105 10 0 0 0 320 1020 L328 960 Z" fill="url(#g-orange)"/>
      <ellipse cx="215" cy="960" rx="113" ry="10" fill="#B9582A"/>
      <text class="stage-label" x="215" y="999">$ + V</text>
    </g>

    <g class="connectors" stroke="var(--corporate-blue)" stroke-width="1.5" fill="none">
      <line x1="313" y1="316" x2="397" y2="316"/>
      <line x1="313" y1="450" x2="397" y2="450"/>
      <line x1="313" y1="568" x2="397" y2="568"/>
      <line x1="313" y1="687" x2="397" y2="687"/>
      <line x1="313" y1="798" x2="397" y2="798"/>
      <line x1="313" y1="897" x2="397" y2="897"/>
      <line x1="313" y1="990" x2="397" y2="990"/>
    </g>
    <g fill="var(--corporate-blue)">
      <circle cx="313" cy="316" r="3.5"/><circle cx="313" cy="450" r="3.5"/><circle cx="313" cy="568" r="3.5"/>
      <circle cx="313" cy="687" r="3.5"/><circle cx="313" cy="798" r="3.5"/><circle cx="313" cy="897" r="3.5"/>
      <circle cx="313" cy="990" r="3.5"/>
    </g>
    <g class="markers" fill="var(--corporate-blue)" stroke="var(--white)" stroke-width="2">
      <circle cx="415" cy="316" r="18"/><circle cx="415" cy="450" r="18"/><circle cx="415" cy="568" r="18"/>
      <circle cx="415" cy="687" r="18"/><circle cx="415" cy="798" r="18"/><circle cx="415" cy="897" r="18"/>
      <circle cx="415" cy="990" r="18"/>
    </g>
    <g fill="none" stroke="var(--corporate-blue)" stroke-width="1.5">
      <circle cx="415" cy="316" r="20"/><circle cx="415" cy="450" r="20"/><circle cx="415" cy="568" r="20"/>
      <circle cx="415" cy="687" r="20"/><circle cx="415" cy="798" r="20"/><circle cx="415" cy="897" r="20"/>
      <circle cx="415" cy="990" r="20"/>
    </g>
    <g>
      <text class="step-number" x="415" y="322">1</text>
      <text class="step-number" x="415" y="456">2</text>
      <text class="step-number" x="415" y="574">3</text>
      <text class="step-number" x="415" y="693">4</text>
      <text class="step-number" x="415" y="804">5</text>
      <text class="step-number" x="415" y="903">6</text>
      <text class="step-number" x="415" y="996">7</text>
    </g>
    <g class="step-text">
      <text x="449" y="320">Clarify vision, goals,</text><text x="449" y="335">values</text>
      <text x="449" y="455">Develop, refine audience,</text><text x="449" y="470">value prop, key messages,</text><text x="449" y="485">differentiators, channels</text>
      <text x="449" y="573">Optimize sales tools,</text><text x="449" y="588">website, overview,</text><text x="449" y="603">pitch deck, technologies</text>
      <text x="449" y="692">Prioritize &amp; execute</text><text x="449" y="707">demand-gen activities,</text><text x="449" y="722">measure, optimize</text>
      <text x="449" y="802">Develop, refine, execute</text><text x="449" y="817">biz dev &amp; sales process,</text><text x="449" y="832">account development,</text><text x="449" y="847">team</text>
      <text x="449" y="901">Past/current client</text><text x="449" y="916">relations, resell, retention</text><text x="449" y="931">and referrals, service</text>
      <text x="449" y="994">Measure, optimize,</text><text x="449" y="1009">build capacity,</text><text x="449" y="1024">accelerate, scale</text>
    </g>
  </svg>

  <div class="brand-name">FERNCROW</div>
  <div class="web-box">www.ferncrow.com</div>
</div>
</body>
</html>
```